New Zealand Export company needs business cards

We need new business cards to match our new logo for a company based in New Zealand who deal specifically with the Pacific Islands. We source, consolidate and ship products out of New Zealand to the Pacific Islands. Will attach our old ones and also new logo.
Would like the Islands we deal with and the areas of work we have access to, to be included on the business cards.

Contact Information for Business Card

T +64 9 571 3048
F +64 9 571 6285
12-18 Kowhai Lane, Drury, 2113
PO Box 814, Drury, Auckland 2247, New Zealand
www.falconfreight.example.nz
E sales@falconfreight.example.nz

Font styles to use
Sans Serif

Colors
85abd2
33a6d7
ffffff

Requirements
Must have
• A company of PWM

```html
<!DOCTYPE html>
<html lang="en">
<head>
<meta charset="utf-8">
<title>Falcon Freight – Business Card</title>
<link rel="stylesheet" href="https://fonts.googleapis.com/css2?family=Montserrat:wght@400;500&family=Oswald:wght@500&display=swap">
<style>
  :root {
    --bg: #2b2b2b;
    --card: #242424;
    --texture-light: #333333;
    --texture-mid: #262626;
    --texture-dark: #1c1c1c;
    --accent: #33a6d7;
    --accent-soft: #85abd2;
    --white: #ffffff;
  }
  * { margin: 0; padding: 0; box-sizing: border-box; }
  html, body { width: 1200px; height: 901px; overflow: hidden; }
  body {
    background: radial-gradient(ellipse at 60% 40%, #3a3a3a 0%, var(--bg) 55%, #1c1c1c 100%);
    font-family: "Montserrat", sans-serif;
    color: var(--white);
    position: relative;
  }
  .card {
    position: absolute;
    left: 300px;
    width: 600px;
    height: 340px;
    background: var(--card);
    box-shadow: 0 16px 34px rgba(0,0,0,.5);
    overflow: hidden;
  }
  .card::after {
    content: "";
    position: absolute;
    left: 0; right: 0; bottom: 0;
    height: 7px;
    background: var(--accent);
  }
  .card--back { top: 60px; }
  .card--front { top: 450px; }

  .back-texture {
    position: absolute;
    inset: 0;
    background:
      radial-gradient(ellipse at 75% 70%, var(--texture-light) 0%, transparent 60%),
      linear-gradient(160deg, var(--texture-mid) 0%, var(--texture-dark) 100%);
  }
  .back-brand {
    position: absolute;
    right: 48px;
    bottom: 48px;
    font-weight: 500;
    font-size: 20px;
    letter-spacing: .5px;
    color: var(--accent);
  }

  .identity {
    position: absolute;
    left: 40px;
    top: 100px;
    width: 248px;
    text-align: right;
  }
  .identity__name {
    font-family: "Oswald", sans-serif;
    font-weight: 500;
    font-size: 50px;
    line-height: 1;
    letter-spacing: 1px;
    text-transform: uppercase;
  }
  .identity__role {
    font-size: 16px;
    color: var(--accent);
    margin-top: 4px;
  }
  .divider {
    position: absolute;
    left: 306px;
    top: 100px;
    width: 2px;
    height: 88px;
    background: var(--accent);
  }
  .contacts {
    position: absolute;
    left: 324px;
    top: 96px;
    list-style: none;
    font-size: 13.5px;
    line-height: 24px;
  }
  .contacts li { display: flex; align-items: center; gap: 8px; white-space: nowrap; }
  .contacts svg { width: 13px; height: 13px; fill: var(--accent); flex: none; }
  .address {
    position: absolute;
    left: 56px;
    top: 254px;
    font-size: 15px;
    line-height: 24px;
  }
  .address span { display: block; white-space: nowrap; }
  .address .street { padding-left: 84px; }
</style>
</head>
<body>
  <section class="card card--back" aria-label="Card back">
    <div class="back-texture" role="img" aria-label="Embossed repeating company monogram texture"></div>
    <div class="back-brand">Falcon Freight</div>
  </section>

  <section class="card card--front" aria-label="Card front">
    <div class="identity">
      <h1 class="identity__name">Aaron Tait</h1>
      <p class="identity__role">Manager</p>
    </div>
    <div class="divider"></div>
    <ul class="contacts">
      <li>
        <svg viewBox="0 0 16 16" aria-hidden="true"><path d="M3.6 1.2l2.3 2.6-1.2 1.8c.9 2 2.5 3.6 4.5 4.6l1.8-1.2 2.6 2.3-1.3 2.7C7 13.6 2.4 9 1 3.6z"/></svg>
        +64 9 571 3048
      </li>
      <li>
        <svg viewBox="0 0 16 16" aria-hidden="true"><path d="M4 1h8v4H4z M1 6h14v6h-3v3H4v-3H1z M5.5 10v3.5h5V10z"/></svg>
        +64 9 571 6285
      </li>
      <li>
        <svg viewBox="0 0 16 16" aria-hidden="true"><path d="M1 3h14v10H1z M2.5 4.5L8 9l5.5-4.5" stroke="#242424" stroke-width="1.2"/></svg>
        sales@falconfreight.example.nz
      </li>
      <li>
        <svg viewBox="0 0 16 16" aria-hidden="true"><circle cx="8" cy="8" r="7"/><path d="M1 8h14M8 1c-3 3-3 11 0 14M8 1c3 3 3 11 0 14" stroke="#242424" stroke-width="1.1" fill="none"/></svg>
        www.falconfreight.example.nz
      </li>
    </ul>
    <p class="address">
      <span class="street">12-18 Kowhai Lane, Drury, 2113</span>
      <span>PO Box 814, Drury, Auckland 2247, New Zealand</span>
    </p>
  </section>
</body>
</html>
```